Need Wordpress business website designed for the website Quarrowden.com

Quarrowden.com needs a Wordpress website to connect mineral rights buyers and sellers from across the United States. This website will be a userfriendly listing service. Below is a list of requirements that need to be accomplished for this project.
-Logo design
-5 to 10 pages of SEO content with copy included. 100-200 words per page.
-Responsive Web design.
-User-friendly add listing page and view listing pages. (2 out of the 7-10 pages needed)
1. Home page
This will have short introduction and possible video plugin.
Welcome to QuarRowden.com. Market your minerals to a large group of investors. By marketing your mineral rights on QuarRowden.com Investors compete so you get a fair market offer.
Contact: 844-317-2906
info@Quarrowden.com
2. Our Service or About us Page
-Get the best price for your mineral rights and oil and gas royalties
-Market your mineral rights to attract the best price possible
-Connect you to reputable mineral rights buyers
-Help you understand the industry and answer all of your questions
Our representatives are here to answer any questions you may have.
3 Add Listing Page
Add listing page will need the following boxes
First Name:
Last Name:
Phone Number:
Email:
State:
County:
Net Acres:
Price Per Acre:
Leased Producing
Legal Description:
Comments:
4 View Listing Page
View listing Page will need the following info:
First Name:
Last Name:
Phone Number:
Email:
State:
County:
Net Acres:
Price Per Acre:
Leased Producing
Legal Description:
Comments:
View listings page will need the following:
Listing Number
State: Insert drop down box or fill in form
County: Insert drop down box or fill in form
Legal Description: Fill in form
Net Acres: Fill in form
Price: Fill in form
Notes:
Date Listed:
Interested in this listing? Call 844-317-2906 or fill out the contact box below.
Contact Box:
First Name
Last Name
Email
Phone Number
Questions/Comments?
5. Why Sell?
Receive an immediate lump sum cash payment now.
-Minimize your risk. Protect yourself from the uncertainties of the industry. (Falling natural gas prices, Shut-in and poor producing wells, Infrastructure and pipeline delays)
-Lower taxes. Your mineral rights sale will be taxed at 20% while royalty and bonus payments are taxed as ordinary income at 35%
-Estate Planning. Eliminate complicated forms such as maintenance and depletion schedules, division order agreements, and 1099’s.
-Diversify your assets while paying down bad debt
-Utilize the 1031 tax exchange to invest in more property tax free.
6. News
Page with news articles.
-Research on most important Keywords needed for site.
-Implementation of meta data and HTML elements of site.
-Implement robot tags where needed.
- Creation of sitemap and submission to search engines.
Google Analytics
-Intall a website traffic statistics program that provides important information about viewership. Need to track daily visitors, top search engines and referral sites, bounce rate, top landing pages, mobile traffic, etc...
Google webmaster tools
-Install webmaster tools to determine health and technical status of website.
Listing distribution service
-website needs listed with all four major listing data providers. Brindlet, Vorthel, pallowset, and Kembrite.
Video Plugin
-Option to include video greeting and instruction on homepage.
Setup of Social Media Accounts
-Google+, Friendwall, and Linkedin Account pages.
Example Webpages:
holdfieldtrader.com
tandrocksbourse.com
grauvenlandings.com
bidtallowcrestlots.com
Target Market(s)
Mineral Rights Owners, Landowners, Mineral Rights Buyers, Oil and Gas Owners, Oil and Gas buyers, Oil and Gas Royalty Owners, Oil and Gas Royalty Buyers, Oil and Gas investors, Mineral Rights Investors.
Industry/Entity Type
Oil And Gas
Font styles to use
Requirements
Must have
- -contact box on the right side
- -Location information on bottom of site.
- -live chat box plugin
- -listing box with the following drop down boxes
- First Name:
- Last Name:
- Phone Number:
- Email:
- State:
- County:
- Net Acres:
- Price Per Acre:
- Leased? Producing?
- Legal Description:
- Comments:
Nice to have
- Video plugin on Home page

```html
<!DOCTYPE html>
<html lang="en">
<head>
<meta charset="utf-8">
<title>Quarrowden – Market Your Minerals</title>
<link rel="stylesheet" href="https://fonts.googleapis.com/css2?family=Open+Sans:wght@300;400;600;700&display=swap">
<style>
:root{
  --red:#d2232a;
  --red-dark:#a9161c;
  --ink:#222;
  --body:#555;
  --grey-bg:#f0f0f0;
  --nav-bg:#1c1c1c;
  --footer-bg:#2e2e2e;
  --footer-base:#232323;
  --white:#fff;
}
*{margin:0;padding:0;box-sizing:border-box}
html,body{width:1200px;height:2913px;overflow:hidden}
body{font-family:"Open Sans",Arial,sans-serif;color:var(--body);background:var(--white);position:relative}
.abs{position:absolute}
.topbar{left:0;top:0;width:1200px;height:74px;background:var(--red)}
.brand{left:99px;top:20px;display:flex;align-items:center;gap:8px;color:var(--white);font-weight:700;font-size:25px}
.brand-mark{width:30px;height:30px;border:3px solid var(--white)}
.top-contact{top:14px;display:flex;align-items:center;gap:12px;color:var(--white)}
.icon-circle{border-radius:50%;background:var(--red-dark);display:flex;align-items:center;justify-content:center}
.top-contact .icon-circle{width:44px;height:44px}
.top-contact small{display:block;font-size:11px}
.top-contact strong{font-weight:400;font-size:17px}
.hero{left:0;top:74px;width:1200px;height:419px;background:linear-gradient(180deg,#5a2430 0%,#9a3b34 35%,#c9583a 60%,#3a1f1f 85%,#1a1212 100%)}
.hero-title{left:569px;top:262px;color:var(--white);font-size:30px;line-height:40px;text-transform:uppercase}
.hero-title b{font-weight:700;display:block}
.hero-title span{font-weight:300;display:block}
.nav{left:0;top:493px;width:1200px;height:68px;background:var(--nav-bg)}
.nav-item{top:493px;height:68px;padding:17px 18px 0;color:var(--white)}
.nav-item b{display:block;font-size:12px;font-weight:700}
.nav-item small{font-size:9px;color:#aaa}
.nav-item.active{background:var(--red)}
.nav-item.active small{color:#fbd}
.quick-form{left:825px;top:493px;width:275px;height:68px;background:var(--red);color:var(--white);padding:16px 22px}
.quick-form b{display:block;font-size:16px;font-weight:700}
.quick-form small{font-size:10px}
.quick-form .tab{position:absolute;right:0;top:0;width:52px;height:68px;background:var(--red-dark);display:flex;align-items:center;justify-content:center}
.video{left:99px;top:627px;width:379px;height:257px;background:linear-gradient(180deg,#6f8fb5 0%,#c7d3e0 45%,#5d7b3a 75%,#3d5a24 100%)}
.video-bar{position:absolute;left:0;bottom:0;width:100%;height:22px;background:#111}
.video-play{position:absolute;left:160px;top:108px;width:62px;height:42px;border-radius:10px;background:var(--red);display:flex;align-items:center;justify-content:center}
.video-shadow{left:120px;top:884px;width:337px;height:14px;border-radius:50%;background:radial-gradient(#bbb,transparent 70%)}
h2{font-size:20px;font-weight:700;color:var(--ink);text-transform:uppercase}
.welcome-title{left:544px;top:670px}
.welcome-text{left:544px;top:716px;width:520px;font-size:12px;line-height:24px}
.contact-pill{top:786px;display:flex;align-items:center;gap:14px}
.contact-pill .icon-circle{width:58px;height:58px;background:var(--red)}
.contact-pill small{display:block;font-size:11px;color:var(--body)}
.contact-pill strong{font-weight:400;font-size:19px;color:var(--red)}
.band-grey{left:0;top:940px;width:1200px;height:503px;background:var(--grey-bg)}
.center{left:0;width:1200px;text-align:center}
.lead{left:150px;width:900px;text-align:center;font-size:13px;line-height:29px}
.feature{top:1132px;width:260px;text-align:center}
.feature .icon-circle{width:120px;height:120px;background:var(--red);margin:0 auto}
.feature h3{margin-top:22px;font-size:15px;font-weight:400;color:var(--red)}
.feature p{margin-top:10px;font-size:11px;line-height:23px;padding:0 20px}
.work{top:1618px;width:235px}
.work-img{width:235px;height:161px}
.work h4{margin-top:22px;font-size:11px;font-weight:700;color:var(--ink)}
.work p{margin-top:6px;font-size:11px;line-height:25px}
.testimonials{left:0;top:1923px;width:1200px;height:380px;background:linear-gradient(90deg,#1d2127 0%,#2c2f33 55%,#3a3530 100%)}
.testimonials h2{color:var(--white)}
.quote-text{left:260px;width:680px;top:2052px;text-align:center;color:var(--white);font-size:12px;line-height:25px}
.quote-mark{color:#ccc;font-size:40px;font-family:Georgia,serif}
.avatar{left:473px;top:2156px;width:84px;height:84px;border-radius:50%;background:linear-gradient(#bbb,#8a8a8a);border:3px solid var(--white)}
.author{left:579px;top:2172px;color:var(--white);font-size:13px;line-height:24px}
.author i{color:#ccc}
.arrow{color:#666;font-size:28px}
.assoc-box{top:2484px;width:130px;height:81px;border:1px solid #ddd;display:flex;align-items:center;justify-content:center}
.assoc-box span{width:80px;height:24px;border-radius:4px;background:#ddd}
.footer{left:0;top:2618px;width:1200px;height:247px;background:var(--footer-bg)}
.footer-base{left:0;top:2865px;width:1200px;height:48px;background:var(--footer-base);text-align:center;color:#888;font-size:10px;line-height:48px}
.f-head{top:2658px;color:var(--white);font-size:12px;font-weight:700;text-transform:uppercase}
.f-text{color:#999;font-size:10px;line-height:22px}
.f-list{list-style:none;color:#999;font-size:10px;line-height:22px}
.social li{display:flex;align-items:center;gap:8px;margin-bottom:1px}
.social i{width:22px;height:22px;border:1px solid #555;display:inline-block}
.map{left:684px;top:2660px;width:242px;height:152px;background:linear-gradient(135deg,#e8e4dc,#d8d6cf)}
.live-chat{left:1031px;top:2587px;width:169px;height:62px;background:var(--red);color:var(--white);display:flex;align-items:center;gap:10px;padding-left:14px}
.live-chat .face{width:38px;height:38px;border-radius:50%;background:#e6c7b7;border:2px solid var(--white)}
.live-chat b{display:block;font-size:12px}
.live-chat small{font-size:8px;font-weight:700}
</style>
</head>
<body>

<header>
  <div class="abs topbar"></div>
  <div class="abs brand"><span class="brand-mark"></span>Quarrowden</div>
  <div class="abs top-contact" style="left:669px">
    <span class="icon-circle"><svg width="20" height="20" viewBox="0 0 24 24"><path fill="#fff" d="M6.6 10.8a15 15 0 0 0 6.6 6.6l2.2-2.2c.3-.3.7-.4 1-.2 1.1.4 2.3.6 3.6.6.6 0 1 .4 1 1V20c0 .6-.4 1-1 1A17 17 0 0 1 3 4c0-.6.4-1 1-1h3.5c.6 0 1 .4 1 1 0 1.3.2 2.5.6 3.6.1.3 0 .7-.2 1z"/></svg></span>
    <div><small>Call Us :</small><strong>844-317-2906</strong></div>
  </div>
  <div class="abs top-contact" style="left:872px">
    <span class="icon-circle"><svg width="20" height="16" viewBox="0 0 24 18"><path fill="#fff" d="M0 0h24v2L12 10 0 2zM0 4l12 8 12-8v14H0z"/></svg></span>
    <div><small>Email Us :</small><strong>info@Quarrowden.com</strong></div>
  </div>
</header>

<section class="abs hero" role="img" aria-label="Pumpjacks silhouetted against a red sunset sky"></section>
<div class="abs hero-title"><b>Market your minerals</b><span>to a large group of investors</span></div>

<nav>
  <div class="abs nav"></div>
  <div class="abs nav-item active" style="left:103px;width:139px"><b>HOME</b><small>Welcome to our site</small></div>
  <div class="abs nav-item" style="left:248px"><b>ADD LISTING</b><small>Add your Listing</small></div>
  <div class="abs nav-item" style="left:392px"><b>VIEW LISTINGS</b><small>View all Listings</small></div>
  <div class="abs nav-item" style="left:526px"><b>TESTIMONIALS</b><small>Clients Feed back</small></div>
  <div class="abs nav-item" style="left:686px"><b>CONTACT US</b><small>Get in touch</small></div>
  <div class="abs quick-form"><b>QUICK CONTACT FORM</b><small>Click here for fill the form</small>
    <span class="tab"><svg width="26" height="26" viewBox="0 0 26 26"><circle cx="13" cy="13" r="11" fill="none" stroke="#fff" stroke-width="2"/><path d="M8 11l5 5 5-5" fill="none" stroke="#fff" stroke-width="2"/></svg></span>
  </div>
</nav>

<section class="welcome">
  <div class="abs video" role="img" aria-label="Video greeting still: clouds over green hills">
    <span class="video-play"><svg width="18" height="20" viewBox="0 0 18 20"><path d="M0 0l18 10L0 20z" fill="#fff"/></svg></span>
    <span class="video-bar"></span>
  </div>
  <div class="abs video-shadow"></div>
  <h2 class="abs welcome-title">Welcome to Quarrowden</h2>
  <p class="abs welcome-text">Welcome to QuarRowden.com. Market your minerals to a large group of investors. By marketing your mineral rights on QuarRowden.com Investors compete so you get a fair market offer.</p>
  <div class="abs contact-pill" style="left:544px">
    <span class="icon-circle"><svg width="24" height="24" viewBox="0 0 24 24"><path fill="#fff" d="M6.6 10.8a15 15 0 0 0 6.6 6.6l2.2-2.2c.3-.3.7-.4 1-.2 1.1.4 2.3.6 3.6.6.6 0 1 .4 1 1V20c0 .6-.4 1-1 1A17 17 0 0 1 3 4c0-.6.4-1 1-1h3.5c.6 0 1 .4 1 1 0 1.3.2 2.5.6 3.6.1.3 0 .7-.2 1z"/></svg></span>
    <div><small>Call Us :</small><strong>844-317-2906</strong></div>
  </div>
  <div class="abs contact-pill" style="left:767px">
    <span class="icon-circle"><svg width="24" height="18" viewBox="0 0 24 18"><path fill="#fff" d="M0 0h24v2L12 10 0 2zM0 4l12 8 12-8v14H0z"/></svg></span>
    <div><small>Email Us :</small><strong>info@Quarrowden.com</strong></div>
  </div>
</section>

<section class="how">
  <div class="abs band-grey"></div>
  <h2 class="abs center" style="top:996px">How it works</h2>
  <p class="abs lead" style="top:1034px">Our service has helped many Mineral Owners get top dollar by putting their mineral rights in front of our large market of mineral rights buyers and investors. Click on the Add Listing button above to get started.</p>
  <div class="abs feature" style="left:144px">
    <div class="icon-circle"><svg width="50" height="40" viewBox="0 0 50 40" fill="#fff"><circle cx="25" cy="10" r="7"/><circle cx="11" cy="14" r="5"/><circle cx="39" cy="14" r="5"/><path d="M13 36c0-9 5-15 12-15s12 6 12 15z"/><path d="M1 34c0-7 4-11 10-11 2 0 3 .5 4 1-2 3-3 6-3 10zM49 34c0-7-4-11-10-11-2 0-3 .5-4 1 2 3 3 6 3 10z"/></svg></div>
    <h3>Mineral Owners</h3>
    <p>Our service has helped many Mineral Owners get top dollar by putting their mineral rights in front of our large market...</p>
  </div>
  <div class="abs feature" style="left:470px">
    <div class="icon-circle"><svg width="44" height="44" viewBox="0 0 44 44" fill="#fff"><path d="M22 2L2 12v4h40v-4z"/><rect x="6" y="18" width="5" height="16"/><rect x="15" y="18" width="5" height="16"/><rect x="24" y="18" width="5" height="16"/><rect x="33" y="18" width="5" height="16"/><rect x="2" y="36" width="40" height="5"/></svg></div>
    <h3>Mineral Rights</h3>
    <p>Our service has helped many Mineral Owners get top dollar by putting their mineral rights in front of our large market...</p>
  </div>
  <div class="abs feature" style="left:795px">
    <div class="icon-circle"><svg width="56" height="40" viewBox="0 0 56 40" fill="none" stroke="#fff" stroke-width="4" stroke-linejoin="round"><path d="M2 10l10-6 10 4 6-2 8 2 10-4 8 6"/><path d="M12 4l-8 18 14 14 4-3 4 3 4-3 4 3 10-10L38 8 26 12l-6 8 6 2 8-6"/></svg></div>
    <h3>Buyers and Investors</h3>
    <p>Our service has helped many Mineral Owners get top dollar by putting their mineral rights in front of our large market...</p>
  </div>
</section>

<section class="what">
  <h2 class="abs center" style="top:1487px">What we do</h2>
  <p class="abs lead" style="top:1526px">Our service has helped many Mineral Owners get top dollar by putting their mineral rights in front of our large market of mineral rights buyers and investors. Click on the Add Listing button above to get started.</p>
  <div class="abs work" style="left:99px"><div class="work-img" role="img" aria-label="Pumpjack at sunset" style="background:linear-gradient(180deg,#3b3b45,#b57a45 60%,#1b1a18)"></div><h4>PUMPJACK</h4><p>Es simplemente el texto de relleno de las imprentas y archivos de texto.</p></div>
  <div class="abs work" style="left:355px"><div class="work-img" role="img" aria-label="Green meadow under a blue sky" style="background:linear-gradient(180deg,#4a86c8,#c9dcef 45%,#7fb13c 65%,#4f8a24)"></div><h4>MEADOW</h4><p>Es simplemente el texto de relleno de las imprentas y archivos de texto.</p></div>
  <div class="abs work" style="left:610px"><div class="work-img" role="img" aria-label="Oil rig beside a dark field" style="background:linear-gradient(180deg,#8fb6e6,#d4e3f4 55%,#2f4a2c 60%,#1e2f1c)"></div><h4>OILRIG</h4><p>Es simplemente el texto de relleno de las imprentas y archivos de texto.</p></div>
  <div class="abs work" style="left:866px"><div class="work-img" role="img" aria-label="Pasture with hills and clouds" style="background:linear-gradient(180deg,#8ea4b8,#d2d9de 45%,#51793a 70%,#2d5224)"></div><h4>PASTURE</h4><p>Es simplemente el texto de relleno de las imprentas y archivos de texto.</p></div>
</section>

<section class="abs testimonials" role="img" aria-label="Oil field worker in a hard hat, darkened backdrop"></section>
<h2 class="abs center" style="top:1988px;color:#fff">Testimonials</h2>
<span class="abs quote-mark" style="left:236px;top:2016px">&ldquo;</span>
<p class="abs quote-text">The representatives at QuarRowden.com helped educate me about the process of selling our mineral rights in Ohio. We learned that the value is determined by a number of factors. We were able to find a mineral rights buyer and close very quickly on our property</p>
<span class="abs quote-mark" style="left:948px;top:2090px">&rdquo;</span>
<span class="abs arrow" style="left:148px;top:2080px">&lsaquo;</span>
<span class="abs arrow" style="left:1040px;top:2080px">&rsaquo;</span>
<div class="abs avatar" role="img" aria-label="Client portrait"></div>
<div class="abs author">Dale R<br><i>Distination</i></div>

<section class="assoc">
  <h2 class="abs center" style="top:2348px">Industry Associations</h2>
  <p class="abs lead" style="top:2388px;font-size:16px;color:#555">Market your minerals to a large group of investors. By marketing your mineral rights on QuarRowden.com Investors compete so you get a fair market offer.</p>
  <span class="abs arrow" style="left:68px;top:2505px;color:#ccc">&lsaquo;</span>
  <div class="abs assoc-box" style="left:99px"><span></span></div>
  <div class="abs assoc-box" style="left:244px"><span></span></div>
  <div class="abs assoc-box" style="left:389px"><span></span></div>
  <div class="abs assoc-box" style="left:534px"><span></span></div>
  <div class="abs assoc-box" style="left:679px"><span></span></div>
  <div class="abs assoc-box" style="left:824px"><span></span></div>
  <div class="abs assoc-box" style="left:969px"><span></span></div>
  <span class="abs arrow" style="left:1122px;top:2505px;color:#ccc">&rsaquo;</span>
</section>

<footer>
  <div class="abs footer"></div>
  <h5 class="abs f-head" style="left:101px">About us</h5>
  <p class="abs f-text" style="left:101px;top:2690px;width:240px">Welcome to QuarRowden.com. Our service has helped many Mineral Owners get top dollar by putting their mineral rights in front of our large market of mineral rights buyers and investors.</p>
  <h5 class="abs f-head" style="left:390px">Welcome</h5>
  <ul class="abs f-list" style="left:390px;top:2690px"><li>Home</li><li>Add listing</li><li>View listings</li><li>Testimonials</li><li>About Us</li><li>Education</li></ul>
  <h5 class="abs f-head" style="left:538px">Follow us</h5>
  <ul class="abs f-list social" style="left:538px;top:2690px"><li><i></i>Friendwall</li><li><i></i>Chirpline</li><li><i></i>Orbitplus</li><li><i></i>Linkcrew</li></ul>
  <div class="abs map" role="img" aria-label="Street map with a pin marking the office">
    <svg style="position:absolute;left:80px;top:26px" width="20" height="28" viewBox="0 0 20 28"><path d="M10 0a10 10 0 0 0-10 10c0 8 10 18 10 18s10-10 10-18A10 10 0 0 0 10 0z" fill="#d2232a"/><circle cx="10" cy="10" r="4" fill="#fff"/></svg>
  </div>
  <h5 class="abs f-head" style="left:961px">Contact info</h5>
  <div class="abs f-text" style="left:961px;top:2688px;width:200px"><b style="color:#ddd">QuarRowden</b><br>2190 Fenwick Ridge Rd #42<br>Harlow, Ohio 44902<br>&#9990; 844-317-2906<br>&#9993; info@Quarrowden.com</div>
  <div class="abs live-chat"><span class="face" role="img" aria-label="Chat agent portrait"></span><div><b>LIVE CHAT</b><small>24 HOURS AVAILABLE</small></div></div>
  <div class="abs footer-base">&copy; 2015. Quarrowden All rights reserved.</div>
</footer>

</body>
</html>
```